Kestrel Cove Camp

We need a web page that details location/distance to Melbourne, the facilities available, the magnificent setting, contact information, history of the area and our background in the industry booking enquiry page linked to our email account, feedback page.
(Refer www.campbrindlepoint.com.au for details and further imagary as we operate in the same facility and Camp Brindle Point Business no longer exists) WE WANT A BETTER WEBSITE THAN THIS!!

```html
<!DOCTYPE html>
<html lang="en">
<head>
<meta charset="utf-8">
<title>Kestrel Cove Camp</title>
<link rel="stylesheet" href="https://fonts.googleapis.com/css2?family=Oswald:wght@300;400&family=Open+Sans:wght@400;700&display=swap">
<style>
  :root {
    --page-bg: #e3ded5;
    --sheet: #ffffff;
    --orange: #f5821f;
    --ink: #231f20;
    --text: #3a3a3a;
    --muted: #555555;
    --rule: #c9c9c9;
    --blue: #1ba1e2;
    --sea: #1d6f9a;
    --grass: #4f7a3a;
    --panel: #c7bebd;
    --navy: #2d5188;
    --map-land: #fbe6cf;
    --map-water: #7fcff0;
  }
  * { box-sizing: border-box; margin: 0; padding: 0; }
  html, body { width: 944px; height: 1200px; overflow: hidden; }
  body { background: var(--page-bg); font-family: "Open Sans", Arial, sans-serif; color: var(--text); position: relative; }
  .sheet { position: absolute; left: 40px; top: 0; width: 864px; height: 1200px; background: var(--sheet); }
  .abs { position: absolute; }
  .heading { font-family: "Oswald", "Arial Narrow", sans-serif; font-weight: 300; color: var(--ink); text-transform: uppercase; letter-spacing: -0.5px; }

  .brand { left: 54px; top: 84px; display: flex; align-items: center; gap: 10px; }
  .brand-dot { width: 40px; height: 40px; border-radius: 50%; background: var(--orange); }
  .brand-name { font-family: "Oswald", sans-serif; font-weight: 400; font-size: 26px; color: var(--orange); text-transform: uppercase; }

  .social { left: 766px; top: 71px; display: flex; gap: 6px; }
  .social span { width: 26px; height: 26px; border-radius: 50%; background: #9a9a9a; display: block; }
  .phone-top { right: 58px; top: 104px; font-family: "Oswald", sans-serif; font-weight: 300; font-size: 22px; color: var(--orange); }

  .main-nav { left: 54px; top: 150px; width: 836px; height: 33px; background: var(--orange); display: flex; align-items: center; padding-left: 13px; }
  .main-nav a { font-family: "Oswald", sans-serif; font-weight: 300; font-size: 16px; color: #fff; text-decoration: none; text-transform: uppercase; margin-right: 31px; letter-spacing: -0.3px; }
  .main-nav a:nth-child(2) { margin-right: 32px; }
  .main-nav a:nth-child(4) { margin-right: 23px; }
  .main-nav a:nth-child(5) { margin-right: 24px; }

  .hero { left: 54px; top: 207px; width: 550px; height: 308px; background: linear-gradient(160deg, var(--sea) 0%, #2b8db5 38%, #d9d2bd 46%, #3d6630 56%, var(--grass) 100%); }
  .thumbs { left: 54px; top: 515px; width: 550px; height: 53px; background: var(--ink); display: flex; }
  .thumbs span { width: 78px; height: 53px; display: block; }
  .thumbs span:nth-child(1) { background: linear-gradient(#8a8f88, #6d6a60); }
  .thumbs span:nth-child(2) { background: linear-gradient(#9aa6a8, #5f5a52); }
  .thumbs span:nth-child(3) { background: linear-gradient(#7c8a6a, #9a5a6a); }

  .news { left: 628px; top: 200px; width: 246px; }
  .news-title { font-size: 32px; display: flex; align-items: center; gap: 10px; }
  .post { padding-bottom: 14px; }
  .post + .post { border-top: 1px solid var(--rule); padding-top: 14px; margin-top: 7px; width: 243px; }
  .post-title { font-size: 21px; color: #555; margin-top: 4px; }
  .post p { font-size: 12px; line-height: 17px; color: var(--text); margin-left: 2px; }
  .post time { display: block; font-size: 12px; font-weight: 700; color: #555; margin: 5px 0 0 2px; }

  .rule { height: 1px; background: var(--rule); left: 54px; width: 830px; }

  .feature { top: 620px; width: 400px; height: 110px; }
  .feature-img { position: absolute; left: 4px; top: 0; width: 104px; height: 104px; border-radius: 50%; }
  .feature-title { position: absolute; left: 127px; top: 0; font-size: 33px; }
  .feature p { position: absolute; left: 128px; top: 43px; width: 222px; font-size: 12px; line-height: 17px; }
  .feature-go { position: absolute; left: 364px; top: 41px; }

  .notice { left: 54px; top: 768px; width: 722px; height: 137px; background: var(--panel); color: #fff; font-weight: 700; font-size: 13px; line-height: 17px; padding: 17px 14px; }
  .notice p + p { margin-top: 14px; }
  .badge { left: 793px; top: 768px; width: 88px; height: 138px; background: var(--navy); }

  .foot-col { top: 950px; }
  .foot-title { font-size: 21px; }
  .booking p { font-size: 12px; line-height: 16px; margin-top: 6px; width: 320px; color: var(--ink); }
  .booking .foot-phone { font-family: "Oswald", sans-serif; font-weight: 300; font-size: 15px; margin-top: 10px; text-transform: uppercase; }
  .divider { width: 1px; background: var(--rule); top: 953px; height: 177px; }
  .map { left: 422px; top: 987px; width: 246px; height: 139px; background: linear-gradient(120deg, var(--map-land) 45%, var(--map-water) 70%); }
  .foot-nav { left: 708px; top: 952px; display: flex; flex-direction: column; gap: 10px; }
  .foot-nav a { font-family: "Oswald", sans-serif; font-weight: 300; font-size: 16px; color: var(--ink); text-decoration: none; text-transform: uppercase; line-height: 19.5px; }

  .site-footer { left: 40px; top: 1166px; width: 864px; height: 34px; background: var(--ink); color: #b5b5b5; font-size: 12px; padding: 9px 8px; }
</style>
</head>
<body>
<div class="sheet"></div>

<header>
  <div class="abs brand"><span class="brand-dot"></span><span class="brand-name">Kestrel Cove Camp</span></div>
  <div class="abs social" aria-label="Social links"><span></span><span></span><span></span><span></span></div>
  <div class="abs phone-top">PHONE US: (03) 5550 1982</div>
  <nav class="abs main-nav">
    <a href="#">Home</a><a href="#">Facilities</a><a href="#">Location</a><a href="#">About the site</a><a href="#">Make a booking</a><a href="#">Contact us</a>
  </nav>
</header>

<main>
  <div class="abs hero" role="img" aria-label="Aerial view of the beach, ocean and grassy campsite"></div>
  <div class="abs thumbs">
    <span role="img" aria-label="Campers on the beach"></span>
    <span role="img" aria-label="Campers wading in the water"></span>
    <span role="img" aria-label="Camper outdoors"></span>
  </div>

  <section class="abs news">
    <h2 class="heading news-title">Latest News
      <svg width="30" height="22" viewBox="0 0 30 22"><path d="M2 8h6l14-7v20L8 14H2z" fill="#231f20"/><path d="M8 14l3 7h4l-2-7z" fill="#231f20"/><path d="M24 7l4-2M24 11h5M24 15l4 2" stroke="#231f20" stroke-width="2"/></svg>
    </h2>
    <article class="post">
      <h3 class="heading post-title">Post Title</h3>
      <p>Nam magna nunc, dictum non laoreet nec, vulputate id mi. Sed tincidunt ligula non nibh mattis blandit ac id lorem. Nam eget odio eu ligula ultricies vehicula.</p>
      <time>20 October, 2014</time>
    </article>
    <article class="post">
      <h3 class="heading post-title">Post Title</h3>
      <p>Nam magna nunc, dictum non laoreet nec, vulputate id mi. Sed tincidunt ligula non nibh mattis blandit ac id lorem. Nam eget odio eu ligula ultricies vehicula.</p>
      <time>20 October, 2014</time>
    </article>
  </section>

  <div class="abs rule" style="top:594px"></div>

  <section class="abs feature" style="left:54px">
    <div class="feature-img" role="img" aria-label="Camp accommodation building with verandah" style="background:linear-gradient(#cfd6d8,#6e7a5a)"></div>
    <h2 class="heading feature-title">Facilities</h2>
    <p>Lorem ipsum dolor sit amet, consectetur adipiscing elit. Curabitur tempus neque at metus ornare egestas. Quisque vel sollicitudin turpis.</p>
    <svg class="feature-go" width="36" height="36" viewBox="0 0 36 36"><circle cx="18" cy="18" r="18" fill="var(--blue)"/><path d="M15 11l7 7-7 7" fill="none" stroke="#fff" stroke-width="3.5"/></svg>
  </section>

  <section class="abs feature" style="left:484px">
    <div class="feature-img" role="img" aria-label="Map of the area around the camp" style="background:linear-gradient(120deg,var(--map-land) 50%,var(--map-water))"></div>
    <h2 class="heading feature-title">Getting There</h2>
    <p>Lorem ipsum dolor sit amet, consectetur adipiscing elit. Curabitur tempus neque at metus ornare egestas. Quisque vel sollicitudin turpis.</p>
    <svg class="feature-go" width="36" height="36" viewBox="0 0 36 36"><circle cx="18" cy="18" r="18" fill="var(--blue)"/><path d="M15 11l7 7-7 7" fill="none" stroke="#fff" stroke-width="3.5"/></svg>
  </section>

  <section class="abs notice">
    <p>Lorem ipsum dolor sit amet, consectetur adipiscing elit. Fusce enim est, pulvinar sit amet elit quis, porttitor sagittis massa. Ut quis dictum nisl, non vulputate arcu. Nunc eu ullamcorper velit. Aenean in mauris dignissim, molestie nisl quis, interdum massa. Donec non efficitur leo, at sagittis justo.</p>
    <p>Vestibulum in maximus est. Praesent tincidunt leo quis nunc congue vehicula. Vivamus blandit viverra odio, a posuere massa suscipit eu. Phasellus sodales risus quis commodo viverra.</p>
  </section>
  <div class="abs badge" role="img" aria-label="Accreditation badge"></div>

  <div class="abs rule" style="top:926px"></div>
</main>

<footer>
  <section class="abs foot-col booking" style="left:57px">
    <h2 class="heading foot-title">Make a booking with us</h2>
    <p>Lorem ipsum dolor sit amet, consectetur adipiscing elit. Fusce enim est, pulvinar sit amet elit quis.</p>
    <p class="foot-phone">Phone us: (03) 5550 1982</p>
  </section>
  <div class="abs divider" style="left:401px"></div>
  <section class="abs foot-col" style="left:421px">
    <h2 class="heading foot-title">Location &amp; Directions</h2>
  </section>
  <div class="abs map" role="img" aria-label="Map with directions to the camp"></div>
  <div class="abs divider" style="left:690px"></div>
  <nav class="abs foot-nav">
    <a href="#">Home</a><a href="#">Facilities</a><a href="#">Location</a><a href="#">About the site</a><a href="#">Make a booking</a><a href="#">Contact us</a>
  </nav>
  <div class="abs site-footer">Copyright © 2014</div>
</footer>
</body>
</html>
```